Brightwell has a great new logo - now we need a website!!

Brightwell has been in business for a long time and needs to start a new era. Additional to other changes being made in the business itself, Brightwell needs an overhaul of its entire branding. PART 1 is COMPLETE - we have our new logo!

Next step... new website! That's where you come in.

Brightwell provides a range of computer related services including computer maintenance, networking, sales & cloud services. We provide onsite (field) and remote support. Our customers range from homes to companies with 100+ computers. We pride ourselves on clear and honest communication.

We are a small business but want a professional yet easy-going look that shows the 'cool' side of having your computer system cared for. The website should exude trustworthiness and professionalism but still get comments like 'modern' and 'smart design'. We want our customers to feel that choosing any other company to maintain their system would be a 'geeky' choice.

We like clear thinking so an uncluttered, well organised structure is appreciated. Obvious references to calling or emailing us would be good so people dont need to search around for our contact details.

We look after both Orvane & Kelvantix operating systems so there needs to be universal appeal rather than a look associated with only one of these two brands.

We want to wow our current clients but also attract new ones so a focus on SEO is a must. And a focus on social media too with links/feeds to Chatterloop, blipcast and Workweave!

Have a look at www.brightwell-tech.com.au so you can see for yourself how much you can help us!

**Breathe new life into Brightwell's online presence!**

(We do have a separate website www.hubloomdesk.com.au that we set as the homepage for our clients - we like how it is but it might need freshening up to match our new site. We will also want our chatterloop page totally made over. You'll probably have other suggestions of things we should be doing. We want to form an ongoing relationship with the right designer!)

(Also, we are open to suggestions regarding the logo size and colour)
Updates

I dont want to cramp anyones creativity but i like this: http://www.quandrelweb.com/demo/themes/wordpress/2011/pebble/

I'm obivously happy to see your own ideas too!

I also like this one: http://layoutmarkt.net/item/zindo-responsive-wordpress-theme/7718205

Clarification: We are looking for a working, implemented website, not just design of the theme. Once the general page layout is done we can do the majority of the content input. But we do want a workable shell with images.

We are open to buying existing themes if that helps. Thanks!

Site also needs email contact form, testimonial submission page, blog (feed to home page), chatterloop like button

Reason: I haven't found the ideal one yet... We want some other designers to send their ideas.

Reason: We need a little more time to make our decision.

Target Market(s)

Mainly small to medium businesses but also homes

Industry/Entity Type

Small Business

Requirements
Must have
• SEO
Social Media
That little address bar icon
R in a circle at the bottom of the site to show we have trademarked our company name
A finished product website with content and images that we can modify ourselves over time.

```html
<!DOCTYPE html>
<html lang="en">
<head>
<meta charset="utf-8">
<title>Brightwell – IT Solutions &amp; Support</title>
<link rel="stylesheet" href="https://fonts.googleapis.com/css2?family=Didact+Gothic&family=Montserrat:wght@600;700&display=swap">
<style>
  :root {
    --blue: #2a86dc;
    --blue-deep: #2166b8;
    --ink: #3a3a3a;
    --ink-soft: #555;
    --muted: #777;
    --page: #f7f7f7;
    --panel: #ffffff;
    --rule: #dcdcdc;
    --band: #3c3c3c;
    --footer-bar: #2b2b2b;
    --nav: #8a8a8a;
  }
  * { box-sizing: border-box; margin: 0; padding: 0; }
  html, body { width: 828px; height: 1200px; overflow: hidden; background: var(--page); }
  body { font-family: "Didact Gothic", "Century Gothic", sans-serif; color: var(--ink); }
  .canvas { position: relative; width: 828px; height: 1200px; overflow: hidden; background: var(--page); }
  .abs { position: absolute; }

  /* header */
  .site-header { position: absolute; left: 0; top: 0; width: 828px; height: 67px; background: var(--page); border-bottom: 2px solid var(--blue-deep); }
  .brand { position: absolute; left: 86px; top: 16px; display: flex; align-items: center; gap: 8px; }
  .brand-dot { width: 34px; height: 34px; border-radius: 50%; background: #3b3b4a; }
  .brand-name { font-family: "Montserrat", sans-serif; font-weight: 700; font-size: 17px; color: #3b3b4a; line-height: 1; }
  .brand-tag { font-size: 8.5px; color: var(--nav); margin-top: 2px; }
  .main-nav { position: absolute; left: 428px; top: 22px; width: 254px; display: flex; gap: 14px; font-size: 9px; color: var(--nav); border-bottom: 1px solid #9aa4b0; padding-bottom: 10px; }
  .main-nav .current { color: #222; font-weight: 700; position: relative; }
  .main-nav .current::after { content: ""; position: absolute; left: 0; right: 0; bottom: -12px; height: 2px; background: var(--blue-deep); }

  /* hero */
  .hero-photo { position: absolute; left: 0; top: 67px; width: 828px; height: 411px;
    background: linear-gradient(100deg, #d8dde3 0%, #eef0f2 30%, #f3f3f1 55%, #d5d7d9 80%, #b9bcc0 100%); }
  .hero-photo::after { content: ""; position: absolute; left: 0; right: 0; bottom: 0; height: 170px;
    background: linear-gradient(180deg, rgba(40,50,70,0) 0%, rgba(30,36,50,.55) 100%); }

  /* content panel */
  .content-panel { position: absolute; left: 66px; top: 384px; width: 696px; height: 519px; background: var(--panel); box-shadow: 0 2px 6px rgba(0,0,0,.12); }
  .panel-accent { position: absolute; left: 31px; top: 0; width: 191px; height: 8px; background: var(--blue); }
  .section-title { position: absolute; font-family: "Montserrat", sans-serif; font-weight: 700; font-size: 30px; line-height: 35px; color: var(--blue); }
  .section-kicker { position: absolute; font-size: 11px; font-style: italic; color: var(--muted); }
  .service { position: absolute; width: 120px; text-align: left; }
  .service-art { width: 110px; height: 68px; border-radius: 4px; }
  .service-label { font-size: 11.5px; line-height: 16px; color: var(--ink-soft); margin-top: 26px; }
  .panel-rule { position: absolute; left: 31px; top: 180px; width: 635px; height: 1px; background: var(--rule); }
  .intro-heading { position: absolute; left: 28px; top: 306px; font-size: 21px; font-weight: 400; color: #333; }
  .intro-copy { position: absolute; left: 30px; top: 343px; width: 445px; font-size: 9.2px; line-height: 15.6px; color: var(--ink-soft); }
  .btn { display: inline-block; background: var(--blue); color: #fff; font-size: 8.5px; text-align: center; }
  .intro-btn { position: absolute; left: 31px; top: 427px; width: 139px; height: 22px; line-height: 22px; }
  .devices-art { position: absolute; left: 524px; top: 294px; width: 142px; height: 156px; border-radius: 6px;
    background: linear-gradient(160deg, #2a2c30 0%, #4b5058 45%, #d9dde2 70%, #2b2d31 100%); }

  /* feedback band */
  .feedback-band { position: absolute; left: 66px; top: 903px; width: 696px; height: 62px; background: var(--band); box-shadow: 0 2px 6px rgba(0,0,0,.15); }
  .feedback-text { position: absolute; left: 32px; top: 14px; font-size: 13.5px; line-height: 16.5px; color: #f2f2f2; }
  .action-thumb { position: absolute; left: 510px; top: 9px; width: 154px; height: 45px; background: linear-gradient(90deg, #3a2e26 0%, #5a4a3c 50%, #2a2420 100%); display: flex; align-items: center; gap: 8px; padding-left: 30px; }
  .action-thumb span { font-family: "Montserrat", sans-serif; font-weight: 600; font-size: 7.5px; color: #fff; letter-spacing: .3px; }

  /* footer */
  .footer-col { position: absolute; top: 980px; }
  .footer-brand { font-family: "Montserrat", sans-serif; font-weight: 700; font-size: 16px; color: var(--blue); }
  .footer-text { font-size: 9px; line-height: 13px; color: var(--ink-soft); }
  .footer-head { font-family: "Montserrat", sans-serif; font-weight: 600; font-size: 8px; color: #333; }
  .contact-row { position: absolute; left: 0; display: flex; align-items: center; gap: 14px; font-size: 9px; line-height: 12px; }
  .contact-dot { width: 26px; height: 26px; border-radius: 50%; background: var(--blue); }
  .contact-row b { font-family: "Montserrat", sans-serif; font-weight: 600; font-size: 8px; color: #222; }
  .contact-row a { color: var(--blue); font-weight: 700; text-decoration: none; }
  .field { display: inline-block; height: 19px; border: 1px solid #c8c8c8; background: linear-gradient(#fff, #eee); font-size: 7.5px; line-height: 17px; padding-left: 6px; color: #333; vertical-align: top; }
  .field-btn { height: 19px; line-height: 19px; margin-left: 3px; vertical-align: top; }
  .footer-rule { height: 1px; background: var(--rule); width: 193px; }
  .hl { color: var(--blue); }
  .social { display: flex; gap: 9px; }
  .social-item { width: 26px; height: 26px; border-radius: 50%; background: #e3e3e3; font-size: 5.2px; color: #333; display: flex; align-items: center; justify-content: center; text-align: center; }

  .legal-bar { position: absolute; left: 0; top: 1160px; width: 828px; height: 40px; background: var(--footer-bar); color: #bbb; font-size: 8.5px; }
  .legal-bar .copy { position: absolute; left: 93px; top: 15px; }
  .legal-nav { position: absolute; left: 341px; top: 15px; display: flex; gap: 14px; }
</style>
</head>
<body>
<div class="canvas">

  <header class="site-header">
    <div class="brand">
      <span class="brand-dot"></span>
      <div>
        <div class="brand-name">Brightwell</div>
        <div class="brand-tag">IT Solutions &amp; Support</div>
      </div>
    </div>
    <nav class="main-nav">
      <span class="current">Home</span><span>About Us</span><span>Services</span><span>Pricing</span><span>Contact Us</span><span>Blog</span>
    </nav>
  </header>

  <div class="hero-photo" role="img" aria-label="Photo of laptops, tablets and phones lined up charging against a white brick wall"></div>

  <main class="content-panel">
    <div class="panel-accent"></div>
    <h1 class="section-title" style="left:29px; top:28px;">How Can We<br>Help You!</h1>
    <p class="section-kicker" style="left:29px; top:115px;">- See our services</p>

    <div class="service" style="left:272px; top:28px;">
      <div class="service-art" role="img" aria-label="Illustration of an open laptop showing a maintenance dashboard" style="background:linear-gradient(180deg,#dfe6ee,#9aa3ad);"></div>
      <p class="service-label" style="padding-left:20px;">Computer<br>Maintenance</p>
    </div>
    <div class="service" style="left:430px; top:28px;">
      <div class="service-art" role="img" aria-label="Illustration of a blue cloud for cloud services" style="width:96px; border-radius:40px; background:radial-gradient(circle,#7fc3ee,#3fa0de);"></div>
      <p class="service-label" style="margin-left:-5px;">Sales and Cloud<br>Services</p>
    </div>
    <div class="service" style="left:556px; top:28px;">
      <div class="service-art" role="img" aria-label="Illustration of computers linked around a central network globe" style="width:96px; background:radial-gradient(circle,#8fc6ea 0%,#e6eef5 60%,#fff 100%);"></div>
      <p class="service-label" style="padding-left:26px;">Networking</p>
    </div>

    <div class="panel-rule"></div>

    <h2 class="section-title" style="left:33px; top:212px;">Who are We</h2>
    <p class="section-kicker" style="left:33px; top:264px;">- See our services</p>

    <h3 class="intro-heading">I.T. Problems Fixed Fast</h3>
    <p class="intro-copy">At <b>Brightwell</b>, we provide a range of computer related services. From new computers to website design &amp; hosting, we can help you with almost any technological need. We specialise in onsite computer installation and network setups.<br>Our customers range from homes to companies with 100+ computers. We pride ourselves on clear and honest communication.</p>
    <a class="btn intro-btn">See What Else We Believe</a>

    <div class="devices-art" role="img" aria-label="Photo of a tablet and two smartphones grouped together"></div>
  </main>

  <section class="feedback-band">
    <p class="feedback-text">Getting feedback and your work approved doesn’t have to be hard<br>See how we make it easier....</p>
    <div class="action-thumb" role="img" aria-label="Video still of a team at work, with a play button">
      <svg width="18" height="18" viewBox="0 0 18 18"><circle cx="9" cy="9" r="8" fill="none" stroke="#fff" stroke-width="1.5"/><path d="M7 5.5 L12.5 9 L7 12.5 Z" fill="#fff"/></svg>
      <span>SEE IT IN ACTION</span>
    </div>
  </section>

  <footer>
    <div class="footer-col" style="left:96px; width:200px;">
      <div class="footer-brand">Brightwell</div>
      <p class="footer-text" style="margin-top:4px;">At <b>Brightwell</b>, we provide a range of computer related services. From new computers to website design &amp; hosting, we can help you with almost any technological need.</p>
      <div class="contact-row" style="top:98px;"><span class="contact-dot"></span><span>Wanna talk?<br><b>Call us at (123)555 0147</b></span></div>
      <div class="contact-row" style="top:131px;"><span class="contact-dot"></span><span>Not a big talker?<br><b>Email us at</b> <a>Brightwell@mailnest.com</a></span></div>
    </div>

    <div class="footer-col" style="left:318px; width:200px; top:990px;">
      <div class="footer-head">Search Us!</div>
      <div style="margin-top:8px;"><span class="field" style="width:152px;">what are you doing?</span><a class="btn field-btn" style="width:35px;">Go</a></div>
      <p class="footer-text" style="margin-top:5px;">Find the service you are after only here<br>On <b>Brightwell</b></p>
      <div class="footer-rule" style="margin-top:14px;"></div>
      <div class="footer-head" style="margin-top:19px;">Still here? <span class="hl">GREAT, We are Hiring!</span></div>
      <p class="footer-text" style="margin-top:7px; padding-left:3px;">We need people with chops to join ou quest for world domination <b class="hl">.Want a job. nerd?</b></p>
    </div>

    <div class="footer-col" style="left:541px; width:200px; top:990px;">
      <div class="footer-head">Subscribe to our Newsletter</div>
      <div style="margin-top:8px;"><span class="field" style="width:145px;">Title line here.......</span><a class="btn field-btn" style="width:46px;">Get it</a></div>
      <p class="footer-text" style="margin-top:5px;">Get our monthly newsletter, Brightwell news and many more.. <b class="hl">Check It OUT NOW</b></p>
      <div class="footer-rule" style="margin-top:14px;"></div>
      <div class="footer-head" style="margin-top:19px; padding-left:3px;">Follow us On These......</div>
      <div class="social" style="margin-top:14px; padding-left:2px;">
        <span class="social-item">Blipcast</span>
        <span class="social-item">Chatter-<br>loop</span>
        <span class="social-item">Pixhive</span>
        <span class="social-item">Vid-<br>stream</span>
        <span class="social-item">
          <svg width="12" height="12" viewBox="0 0 12 12"><circle cx="2" cy="10" r="1.6" fill="#333"/><path d="M1 5.5a5.5 5.5 0 0 1 5.5 5.5M1 1.5a9.5 9.5 0 0 1 9.5 9.5" fill="none" stroke="#333" stroke-width="1.6"/></svg>
        </span>
      </div>
    </div>

    <div class="legal-bar">
      <span class="copy">Brightwell&nbsp; Copyrights 2012, All Rights Reserved</span>
      <nav class="legal-nav"><span>Home</span><span>Services</span><span>About Us</span><span>Contact Us</span></nav>
    </div>
  </footer>

</div>
</body>
</html>
```